Automotive parts Package (box) design

We are developing a new packaging concept for our automotive service and suspension parts line. I will share 2–3 sample designs—some from other brands and some AI‑generated—and we need a designer to create a unified, original design direction based on these references.

We already have an established brand name, KEM, along with a logo. The logo may be updated or redesigned, but the brand name KEM must remain.

- The project includes creating the full packaging design for our product boxes, developing or refining the logo if needed.

-Then, after choosing the design, we will apply the same design to 8 boxes with small customisation for each box to match the product.

- The box die-lines will be provided by us.

Attached are a few sample designs. We need you to develop three or more new designs in a similar style. If you have additional creative concepts beyond these references, you are welcome to include them. The only fixed requirement is that the brand name KEM must remain unchanged in all proposed designs.

Box files such as PNG, PDF (ready-to-print file) and Ai (Editable/ Source file) and fonts with 3D mockup images at the end of the project must be given to us.

Target Market(s)

Car spare parts shops

Industry/Entity Type

Auto Parts

Requirements
Must have
• Our brand name KEM
Nice to have
• Package similar to big auto parts suppliers such as PLW, VARNE

```html
<!DOCTYPE html>
<html lang="en">
<head>
<meta charset="UTF-8">
<title>KEM Service Parts – Box Panels</title>
<link rel="stylesheet" href="https://fonts.googleapis.com/css2?family=Archivo+Black&family=Montserrat:wght@400&display=swap">
<style>
  :root {
    --backdrop: #eeeee6;
    --kraft: #c99a6b;
    --kraft-deep: #b98a5c;
    --ink: #0a0a0a;
    --band: #000000;
    --band-text: #d9a272;
    --accent: #d21f26;
  }
  * { margin: 0; padding: 0; box-sizing: border-box; }
  html, body {
    width: 1200px; height: 1200px; overflow: hidden;
    background: var(--backdrop);
  }
  .box-flat {
    position: absolute; left: 100px; top: 90px;
    width: 1000px; height: 1020px;
    display: flex; flex-direction: column;
    box-shadow: 0 18px 40px rgba(0,0,0,0.12);
  }
  .panel {
    position: relative;
    background: radial-gradient(ellipse at 40% 35%, var(--kraft) 0%, var(--kraft-deep) 100%);
  }
  .panel-top { height: 560px; }
  .panel-front { height: 360px; }
  .band {
    height: 100px; background: var(--band);
    display: flex; align-items: center; justify-content: center;
  }
  .band-text {
    font-family: "Montserrat", sans-serif; font-weight: 400;
    font-size: 44px; letter-spacing: 1px; color: var(--band-text);
  }
  .brand {
    position: absolute; display: flex; flex-direction: column;
    font-family: "Archivo Black", sans-serif; color: var(--ink);
  }
  .brand-name { display: flex; align-items: center; gap: 10px; font-size: 72px; line-height: 0.9; letter-spacing: 2px; }
  .brand-mark { width: 18px; height: 18px; background: var(--accent); }
  .brand-tagline { font-size: 13px; letter-spacing: 0.5px; margin-top: 6px; padding-left: 28px; }
  .panel-top .brand { left: 50px; top: 50px; }
  .panel-front .brand { left: 40px; top: 30px; }
  .panel-front .brand-name { font-size: 54px; }
  .panel-front .brand-tagline { font-size: 11px; }
  .headline {
    position: absolute; left: 0; right: 0; text-align: center;
    font-family: "Archivo Black", sans-serif; color: var(--ink);
    letter-spacing: 3px;
  }
  .panel-top .headline { top: 230px; font-size: 78px; }
  .panel-front .headline { top: 150px; font-size: 66px; }
  .warranty-seal { position: absolute; }
  .panel-top .warranty-seal { right: 50px; bottom: 40px; width: 130px; height: 130px; }
  .panel-front .warranty-seal { right: 40px; bottom: 30px; width: 100px; height: 100px; }
</style>
</head>
<body>
  <main class="box-flat">
    <section class="panel panel-top">
      <div class="brand">
        <div class="brand-name"><span class="brand-mark"></span>KEM</div>
        <div class="brand-tagline">AUTOMOTIVE COMPONENTS</div>
      </div>
      <h1 class="headline">SERVICE PARTS</h1>
      <svg class="warranty-seal" viewBox="0 0 100 100" role="img" aria-label="Warranty seal">
        <circle cx="50" cy="50" r="48" fill="var(--ink)"/>
        <circle cx="50" cy="50" r="36" fill="none" stroke="var(--kraft)" stroke-width="2"/>
      </svg>
    </section>
    <div class="band">
      <span class="band-text">KEM AUTOMOTIVE COMPONENTS</span>
    </div>
    <section class="panel panel-front">
      <div class="brand">
        <div class="brand-name"><span class="brand-mark"></span>KEM</div>
        <div class="brand-tagline">AUTOMOTIVE COMPONENTS</div>
      </div>
      <h2 class="headline">SERVICE PARTS</h2>
      <svg class="warranty-seal" viewBox="0 0 100 100" role="img" aria-label="Warranty seal">
        <circle cx="50" cy="50" r="48" fill="var(--ink)"/>
        <circle cx="50" cy="50" r="36" fill="none" stroke="var(--kraft)" stroke-width="2"/>
      </svg>
    </section>
  </main>
</body>
</html>
```